Construction machinery rental / heavy equipment rental needs a nice billboard

We need a billboard for our company.
We rent out construction machinery such as excavators, wheel loaders, wheel dumpers and so on...

I would like an elegant, simple, dark design.
Colors: black yellow grey white

The following must be on the billboard:
Logo
phone number: 078 / 513 90 41
website: www.kiesgrube-talwerk.ch
the machines I rent out: Bagger bis 10T, Radlader, Dumper, Raupenkipper

the font in the logo is: Square 721

Final format 2950 x 1900mm
I have uploaded pictures:
"Excavator 1-6" are my pictures, which can be used
"Sample 1-4" are pictures whose style I like
"Billboard" are billboards which I like

Requirements
Must have
• The following must be on the billboard: Logo phone number: 078 / 513 90 41 website: www.kiesgrube-talwerk.ch the machines I rent out: Bagger bis 10T, Radlader, Dumper, Raupenkipper

```html
<!DOCTYPE html>
<html lang="de">
<head>
<meta charset="utf-8">
<title>Talwerk Baumaschinen – Billboard</title>
<link rel="stylesheet" href="https://fonts.googleapis.com/css2?family=Archivo:ital,wght@1,700;1,800&family=Open+Sans:ital,wght@0,800;1,600&display=swap">
<style>
  :root {
    --black: #050505;
    --gold: #d6bb00;
    --gold-dark: #8a7a1e;
    --grey-light: #f1f1f1;
    --grey-dark: #a9a9a9;
    --olive: rgba(58, 54, 10, 0.82);
    --white: #ffffff;
    --ink: #0b0b0b;
  }
  * { margin: 0; padding: 0; box-sizing: border-box; }
  html, body { width: 1200px; height: 881px; overflow: hidden; background: var(--black); }
  .billboard { position: relative; width: 1200px; height: 881px; background: var(--black); overflow: hidden; }
  .scene-photo { position: absolute; inset: 0; }
  .brand {
    position: absolute; left: 58px; top: 96px;
    display: flex; align-items: center; gap: 14px;
    font-family: "Archivo", sans-serif; font-style: italic; font-weight: 800;
    color: var(--gold); font-size: 58px; letter-spacing: 2px; text-transform: uppercase;
  }
  .brand-mark { width: 40px; height: 40px; background: var(--gold); }
  .machine-list { position: absolute; left: 0; top: 0; width: 100%; height: 100%; }
  .machine-label {
    position: absolute; left: 65px;
    font-family: "Archivo", sans-serif; font-style: italic; font-weight: 700;
    font-size: 41px; line-height: 65px; color: var(--ink); letter-spacing: 0.5px;
  }
  .machine-label::before { content: "•"; margin-right: 16px; font-style: normal; }
  .phone {
    position: absolute; left: 80px; top: 650px;
    font-family: "Open Sans", sans-serif; font-weight: 800;
    font-size: 96px; line-height: 140px; color: var(--gold); letter-spacing: 1px;
  }
  .website {
    position: absolute; left: 63px; top: 800px;
    font-family: "Open Sans", sans-serif; font-style: italic; font-weight: 600;
    font-size: 24px; letter-spacing: 6px; color: var(--white);
  }
</style>
</head>
<body>
<main class="billboard">
  <svg class="scene-photo" width="1200" height="881" viewBox="0 0 1200 881" role="img" aria-label="Nachtaufnahme eines Minibaggers mit Fahrer, der mit hellen Scheinwerfern in Erdreich gräbt">
    <defs>
      <radialGradient id="glow" cx="0.78" cy="0.52" r="0.55">
        <stop offset="0" stop-color="#b9d4e0"/>
        <stop offset="0.18" stop-color="#4d6b6e"/>
        <stop offset="0.5" stop-color="#273226"/>
        <stop offset="1" stop-color="#0a0c08"/>
      </radialGradient>
      <linearGradient id="fade" x1="0" x2="1" y1="0" y2="0">
        <stop offset="0" stop-color="#050505" stop-opacity="1"/>
        <stop offset="0.35" stop-color="#050505" stop-opacity="0.85"/>
        <stop offset="0.6" stop-color="#050505" stop-opacity="0"/>
      </linearGradient>
      <linearGradient id="ground" x1="0" x2="0" y1="0" y2="1">
        <stop offset="0" stop-color="#3f3f22" stop-opacity="0"/>
        <stop offset="1" stop-color="#2c2a14" stop-opacity="0.8"/>
      </linearGradient>
    </defs>
    <rect width="1200" height="881" fill="url(#glow)"/>
    <rect y="520" width="1200" height="361" fill="url(#ground)"/>
    <rect width="1200" height="881" fill="url(#fade)"/>
  </svg>

  <div class="brand"><span class="brand-mark"></span>Talwerk Baumaschinen</div>

  <svg class="machine-list" width="1200" height="881" viewBox="0 0 1200 881" aria-hidden="true">
    <defs>
      <linearGradient id="barGrey" x1="0" x2="1">
        <stop offset="0" stop-color="var(--grey-light)"/>
        <stop offset="1" stop-color="var(--grey-dark)"/>
      </linearGradient>
      <linearGradient id="barGold" x1="0" x2="1">
        <stop offset="0" stop-color="var(--gold)"/>
        <stop offset="1" stop-color="var(--gold-dark)"/>
      </linearGradient>
    </defs>
    <polygon points="0,265 500,265 462,330 0,330" fill="url(#barGrey)"/>
    <polygon points="0,362 478,362 440,427 0,427" fill="url(#barGold)"/>
    <polygon points="0,459 382,459 344,524 0,524" fill="url(#barGrey)"/>
    <polygon points="0,556 478,556 440,621 0,621" fill="url(#barGold)"/>
    <polygon points="0,654 966,654 872,786 0,786" fill="var(--olive)"/>
    <polygon points="1000,654 1022,654 936,786 914,786" fill="var(--white)"/>
    <polygon points="1056,654 1078,654 992,786 970,786" fill="var(--white)"/>
    <polygon points="1112,654 1134,654 1048,786 1026,786" fill="var(--white)"/>
  </svg>

  <div class="machine-label" style="top:265px">BAGGER BIS 10T</div>
  <div class="machine-label" style="top:362px">RADLADER</div>
  <div class="machine-label" style="top:459px">DUMPER</div>
  <div class="machine-label" style="top:556px">RAUPENKIPPER</div>

  <div class="phone">078 / 513 90 41</div>
  <div class="website">www.kiesgrube-talwerk.ch</div>
</main>
</body>
</html>
```